Talcott Land Surveyors Business Card

We are a land surveying company looking for a business card with a clean, sharp design. We would like for our design to portray our logo on one side, and contact information on the other w/ or w/o logo. Our colors preferred are navy blue, grey/silver, white and black. thank you!

Industry/Entity Type

Surveyor

Contact Information for Business Card

Talcott Land Surveyors
Gordon Pavlikova, P.L.S.
(781) 555-0193
Talcottlandsurveyors@mailbox.example
Talcottlandsurveyors.example
287 Willowmere Lane, Reading MA 01999

Requirements
Must have
• 1. Company Name
2. Personal name and title
3. phone number
4. email.
5. website
6. address

```html
<!DOCTYPE html>
<html lang="en">
<head>
<meta charset="utf-8">
<title>Talcott Land Surveyors – Business Card</title>
<link href="https://fonts.googleapis.com/css2?family=Lato:wght@400;700;900&display=swap" rel="stylesheet">
<style>
  :root {
    --navy: #2b3590;
    --navy-soft: #3a44a0;
    --grey: #6f6f73;
    --line: #7b80c4;
    --white: #ffffff;
    --backdrop: #e9e9ec;
  }
  * { box-sizing: border-box; margin: 0; padding: 0; }
  html, body { width: 1200px; height: 1108px; overflow: hidden; }
  body {
    background: var(--backdrop);
    font-family: "Lato", sans-serif;
    position: relative;
  }
  .card {
    position: absolute;
    top: 209px;
    width: 420px;
    height: 690px;
    border-radius: 26px;
    overflow: hidden;
    box-shadow: 0 10px 30px rgba(0,0,0,0.12);
  }
  .card-front { left: 150px; background: var(--white); text-align: center; }
  .card-back { left: 630px; background: var(--navy); }

  .brand {
    margin-top: 190px;
    display: flex;
    align-items: center;
    justify-content: center;
    gap: 12px;
  }
  .brand-dot {
    width: 22px; height: 22px; border-radius: 50%;
    background: var(--navy);
  }
  .brand-name {
    font-weight: 900;
    font-size: 25px;
    letter-spacing: 1.5px;
    color: var(--navy);
    text-transform: uppercase;
    line-height: 1.15;
  }
  .person-name {
    margin-top: 88px;
    font-weight: 900;
    font-size: 27px;
    color: var(--navy);
  }
  .person-title {
    margin-top: 4px;
    font-size: 19px;
    color: var(--grey);
  }
  .icon-rule {
    margin: 16px auto 0;
    width: 320px;
    display: flex;
    align-items: center;
    gap: 6px;
  }
  .icon-rule .rule { flex: 1; height: 1.5px; background: var(--line); }
  .icon { width: 28px; height: 28px; }
  .contact {
    margin-top: 12px;
    font-size: 19px;
    line-height: 1.45;
    color: var(--grey);
  }
  .contact .phone { font-size: 22px; }
  .divider {
    margin: 20px auto 14px;
    width: 310px; height: 1.5px; background: var(--line);
  }
  .address { font-size: 21px; line-height: 1.35; color: var(--grey); }

  .pattern-field {
    position: absolute; inset: 0;
    background: linear-gradient(200deg, #3a44a2 0%, #323c98 45%, var(--navy) 75%);
  }
  .back-mark {
    position: absolute;
    left: 0; right: 0; top: 430px;
    display: flex; flex-direction: column; align-items: center; gap: 10px;
  }
  .back-mark .brand-dot { background: var(--white); width: 18px; height: 18px; }
  .back-mark .brand-name { color: var(--white); font-size: 18px; font-weight: 900; }
</style>
</head>
<body>
  <section class="card card-front">
    <div class="brand">
      <span class="brand-dot"></span>
      <span class="brand-name">Talcott<br>Land Surveyors</span>
    </div>
    <h1 class="person-name">Gordon Pavlikova, P.L.S.</h1>
    <p class="person-title">Founder &amp; CEO</p>
    <div class="icon-rule">
      <span class="rule"></span>
      <svg class="icon" viewBox="0 0 28 28" aria-label="phone">
        <circle cx="14" cy="14" r="13" fill="var(--navy)"/>
        <path d="M9 8c1-1 2-1 3 0l1.5 2.5c.4.8 0 1.5-.7 2l-.8.6c.8 1.8 2 3 3.7 3.8l.6-.8c.5-.7 1.3-1 2-.6L20.8 17c1 1 1 2 0 3-1.2 1.2-3 1.4-5 .4-3.2-1.6-5.6-4-7-7.2-.8-2-.7-3.9.2-5.2z" fill="var(--white)"/>
      </svg>
      <svg class="icon" viewBox="0 0 28 28" aria-label="email">
        <circle cx="14" cy="14" r="13" fill="var(--navy)"/>
        <rect x="7" y="9" width="14" height="10" fill="none" stroke="var(--white)" stroke-width="1.6"/>
        <path d="M7 9l7 6 7-6M7 19l5-5M21 19l-5-5" fill="none" stroke="var(--white)" stroke-width="1.4"/>
      </svg>
      <svg class="icon" viewBox="0 0 28 28" aria-label="website">
        <circle cx="14" cy="14" r="13" fill="var(--navy)"/>
        <circle cx="14" cy="14" r="7.5" fill="none" stroke="var(--white)" stroke-width="1.4"/>
        <ellipse cx="14" cy="14" rx="3.2" ry="7.5" fill="none" stroke="var(--white)" stroke-width="1.2"/>
        <path d="M6.5 14h15M8 10h12M8 18h12" stroke="var(--white)" stroke-width="1.1"/>
      </svg>
      <span class="rule"></span>
    </div>
    <div class="contact">
      <p class="phone">(781) 555-0193</p>
      <p>Talcottlandsurveyors@mailbox.example</p>
      <p>www.talcottlandsurveyors.example</p>
    </div>
    <div class="divider"></div>
    <p class="address">287 Willowmere Lane,<br>Reading MA 01999</p>
  </section>

  <section class="card card-back">
    <div class="pattern-field" role="img" aria-label="Repeating faint pattern of the company mark across the navy back"></div>
    <div class="back-mark">
      <span class="brand-dot"></span>
      <span class="brand-name">Talcott Land Surveyors</span>
    </div>
  </section>
</body>
</html>
```